Physician House Call Doctor

I need 2 newspaper color display adds. 1 small and 1 larger. I have attached some ideas but they need to be updated, more professional and eye-catching . I may also want to change the doctors picture and add some text. I need submit to newspaper in a PDF format and the adds must have a border.

```html
<!DOCTYPE html>
<html lang="en">
<head>
<meta charset="utf-8">
<title>Physician House Calls – Newspaper Ads</title>
<link href="https://fonts.googleapis.com/css2?family=Open+Sans:wght@400;600;700;800&display=swap" rel="stylesheet">
<style>
  :root{
    --sky:#2a8fcb;
    --sky-bright:#0fb2e6;
    --navy:#1b3a6b;
    --navy-deep:#162f57;
    --white:#ffffff;
    --ink:#1a1a1a;
    --stage:#6b6b6b;
  }
  *{margin:0;padding:0;box-sizing:border-box}
  html,body{width:1200px;height:994px;overflow:hidden}
  body{
    background:radial-gradient(ellipse at 40% 20%,#8a8a8a 0%,#6a6a6a 50%,#555 100%);
    font-family:"Open Sans",Arial,sans-serif;
    position:relative;
  }
  .ad{position:absolute;background:var(--white);overflow:hidden;box-shadow:0 6px 18px rgba(0,0,0,.45)}
  .ad svg.bands{position:absolute;left:0;top:0}
  .txt{position:absolute;left:0;width:100%;text-align:center;white-space:nowrap}

  /* large ad */
  .ad-large{left:57px;top:59px;width:680px;height:879px}
  .ad-large .kicker{top:46px;font-size:45px;font-weight:700;color:var(--sky);letter-spacing:.5px;line-height:46px}
  .ad-large .headline{font-size:61px;font-weight:800;color:var(--navy);line-height:62px;letter-spacing:.5px}
  .ad-large .h1{top:102px}
  .ad-large .h2{top:163px}
  .photo{position:absolute;border-radius:50%;background:radial-gradient(circle at 50% 40%,#cfd3d6 0%,#9aa3a8 45%,#5d676d 100%)}
  .ad-large .photo{left:364px;top:264px;width:266px;height:266px}
  .ring{position:absolute;border-radius:50%;border:1.5px solid var(--navy);border-left-color:transparent;border-top-color:transparent;transform:rotate(10deg)}
  .ad-large .ring{left:352px;top:252px;width:290px;height:290px}
  .badge-text{position:absolute;left:80px;top:327px;width:210px;text-align:center;color:var(--navy)}
  .badge-text .name{font-size:15.5px;font-weight:700;line-height:22px}
  .badge-text .role{font-size:12px;color:var(--ink);line-height:18px}
  .badge-text .cert{font-size:14px;font-weight:700;line-height:19px;margin-top:4px}
  .badge-text .note{font-size:10px;color:var(--ink);line-height:16px;margin-top:4px}
  .pitch{position:absolute;left:64px;top:515px;color:var(--white);font-weight:700;font-size:24.5px;line-height:33.5px}
  .hours{top:662px;color:var(--white);font-size:13.5px;line-height:16px}
  .mmj{top:684px;color:var(--white);font-size:13.5px;font-weight:700;line-height:16px}
  .cta{position:absolute;border:1px solid #d7e3f0;border-radius:10px;
    background:linear-gradient(#8ea2bf 0%,#3f5c8c 30%,var(--navy) 55%,var(--navy-deep) 100%);color:var(--white);text-align:center}
  .ad-large .cta{left:50px;top:713px;width:579px;height:99px}
  .cta .num{font-size:52px;font-weight:800;line-height:56px;margin-top:10px;letter-spacing:.5px}
  .cta .sub{font-size:19px;font-weight:700;line-height:22px}
  .fine{top:825px;color:var(--white);font-size:10px;line-height:14px;white-space:normal;padding:0 30px}

  /* small ad */
  .ad-small{left:790px;top:279px;width:340px;height:439px}
  .ad-small .kicker{left:38px;width:auto;text-align:left;top:25px;font-size:29px;font-weight:700;color:var(--sky);line-height:32px}
  .ad-small .kicker2{left:38px;width:auto;text-align:left;top:55px;font-size:29px;font-weight:800;color:var(--navy);line-height:32px}
  .ad-small .doc{left:38px;width:auto;text-align:left;top:103px;font-size:24px;font-weight:700;color:var(--ink);line-height:28px}
  .ad-small .comes{left:38px;width:auto;text-align:left;top:136px;font-size:16px;color:var(--sky);line-height:20px}
  .ad-small .photo{left:178px;top:153px;width:136px;height:136px}
  .ad-small .ring{left:171px;top:146px;width:150px;height:150px}
  .ad-small .cred{left:37px;width:auto;text-align:left;top:242px;font-size:15px;font-weight:700;color:var(--white);line-height:22px;white-space:normal}
  .ad-small .cta{left:30px;top:297px;width:280px;height:49px;border-radius:6px}
  .ad-small .cta .num{font-size:36px;margin-top:4px;line-height:40px}
  .ad-small .info{color:var(--white);font-size:11px;line-height:16px}
  .ad-small .i1{top:355px}
  .ad-small .i2{top:371px}
  .ad-small .i3{top:394px;font-weight:700;font-size:11.5px}
  .ad-small .web{top:413px;font-size:13px;letter-spacing:3px;color:var(--white);line-height:16px}
</style>
</head>
<body>

<section class="ad ad-large">
  <svg class="bands" width="680" height="879" viewBox="0 0 680 879">
    <polygon points="0,253 680,445 680,879 0,879" fill="var(--navy)"/>
    <polygon points="0,333 680,460 680,879 0,879" fill="var(--sky)"/>
    <path d="M120,270 C170,240 260,250 330,300 C380,335 345,420 290,445 C220,470 130,470 95,440 C60,405 75,300 120,270 Z" fill="var(--navy)"/>
    <path d="M95,330 C150,280 260,275 310,310 C355,345 330,430 250,445 C170,458 85,450 48,410 C35,390 60,360 95,330 Z" fill="var(--sky-bright)"/>
    <path d="M100,325 C160,285 260,285 305,318 C340,345 320,420 250,432 C175,442 95,440 62,405 C50,390 70,350 100,325 Z" fill="var(--white)"/>
  </svg>

  <p class="txt kicker">PHYSICIAN HOUSE CALLS</p>
  <p class="txt headline h1">AFFORDABLE</p>
  <p class="txt headline h2">AND CONVENIENT</p>

  <div class="badge-text">
    <p class="name">Daniel R. Whitford, MD</p>
    <p class="role">Primary and Urgent Care</p>
    <p class="cert">Board Certified<br>Family Medicine</p>
    <p class="note">Keep this ad handy for future reference</p>
  </div>

  <div class="ring"></div>
  <div class="photo" role="img" aria-label="Portrait photo of the doctor in a white coat with stethoscope"></div>

  <p class="pitch">Can't get to the doctor<br>or your Doctor can't see<br>you right away, Dr. will come to you.<br>He is Maple Grove and the surrounding area!</p>

  <p class="txt hours">Convenient Daytime Hours and Open most evenings, weekends, and holidays!</p>
  <p class="txt mmj">MEDICINAL MARIJUANA RECOMMENDATION IS NOW AVAILABLE IN MARYLAND.</p>

  <div class="cta">
    <p class="num">CALL: 202-555-0147</p>
    <p class="sub">or visit www.capitalcarehome.com for more information</p>
  </div>

  <p class="txt fine">Medicare is accepted for qualified patients, you pay a small trip fee for your house call. Dr. Whitford does family consults, second opinions medical testing and evaluations.  We also offer Lab Testing, X-rays Breathing Treatments all in the comfort of your home.</p>
</section>

<section class="ad ad-small">
  <svg class="bands" width="340" height="439" viewBox="0 0 340 439">
    <polygon points="0,161 340,257 340,439 0,439" fill="var(--navy)"/>
    <polygon points="0,201 340,261 340,439 0,439" fill="var(--sky)"/>
  </svg>

  <p class="txt kicker">PHYSICIAN HOUSE</p>
  <p class="txt kicker2">CALLS ARE BACK !</p>
  <p class="txt doc">Dr. Daniel R Whitford</p>
  <p class="txt comes">Comes to your home!</p>

  <div class="ring"></div>
  <div class="photo" role="img" aria-label="Portrait photo of the doctor in a white coat with stethoscope"></div>

  <p class="txt cred">Board Certified<br>Family Practice</p>

  <div class="cta"><p class="num">202-555-0147</p></div>

  <p class="txt info i1"><b>Flu Shots</b> now available</p>
  <p class="txt info i2">Why go out in the <b>rain or snow?</b></p>
  <p class="txt info i3">Medicare accepted for qualified patients</p>
  <p class="txt web">www.<b>CapitalCareHome</b>.com</p>
</section>

</body>
</html>
```